"Jewelry Line Postcard Design"

Would like to describe what the line is about via a bio include a photo of me and the logo.

Target Market(s)

20-55

Industry/Entity Type

Jewelry

```html
<!DOCTYPE html>
<html lang="en">
<head>
<meta charset="utf-8">
<title>Lumeria – Jewelry Line Postcard</title>
<link rel="stylesheet" href="https://fonts.googleapis.com/css2?family=Source+Sans+3:ital,wght@0,300;0,400;0,700;1,400&family=Bodoni+Moda:ital,wght@1,400&display=swap">
<style>
  :root {
    --backdrop: #e9eaeb;
    --white: #ffffff;
    --purple: #7b3f98;
    --purple-panel: #8b4a9c;
    --green: #8dbf3f;
    --teal: #2bb38d;
    --ink: #111111;
    --photo-top: #c9c9cb;
    --photo-bottom: #a7a6a8;
  }
  * { box-sizing: border-box; margin: 0; padding: 0; }
  html, body {
    width: 1200px; height: 1000px; overflow: hidden;
    background: var(--backdrop);
  }
  .postcard {
    position: absolute; left: 52px; top: 75px;
    width: 1096px; height: 850px;
    background: var(--white);
    box-shadow: 3px 4px 8px rgba(0,0,0,.35);
    overflow: hidden;
  }
  .logo-panel {
    position: absolute; left: 0; top: 0; width: 634px; height: 253px;
    background: var(--white);
    display: flex; align-items: center; justify-content: center;
  }
  .brand-name {
    font-family: "Source Sans 3", sans-serif;
    font-weight: 300; font-size: 54px; letter-spacing: 10px;
    color: var(--ink);
  }
  .quote-panel {
    position: absolute; left: 637px; top: 0; width: 459px; height: 253px;
    background: var(--purple);
  }
  .quote-box {
    position: absolute; left: 646px; top: 37px; width: 450px; height: 200px;
    background: var(--teal);
    border-radius: 22px 0 0 22px;
    box-shadow: 2px 4px 6px rgba(0,0,0,.3);
    display: flex; align-items: center; justify-content: center;
    padding: 0 14px;
  }
  .quote-text {
    font-family: "Bodoni Moda", serif; font-style: italic;
    font-size: 19px; line-height: 28px; color: var(--white);
    text-align: center; white-space: nowrap;
  }
  .bio-panel {
    position: absolute; left: 0; top: 256px; width: 634px; height: 594px;
    background: var(--green);
  }
  .bio-box {
    position: absolute; left: 0; top: 272px; width: 616px; height: 533px;
    background: var(--purple-panel);
    border-radius: 0 24px 24px 0;
    box-shadow: 3px 4px 6px rgba(0,0,0,.3);
    padding: 4px 0 0 46px;
  }
  .bio-text {
    font-family: "Source Sans 3", sans-serif;
    font-size: 19px; line-height: 28.8px; color: var(--white);
    text-indent: 35px; white-space: nowrap;
  }
  .bio-text strong { font-weight: 700; }
  .portrait {
    position: absolute; left: 637px; top: 256px; width: 459px; height: 594px;
    background: linear-gradient(180deg, var(--photo-top), var(--photo-bottom));
  }
</style>
</head>
<body>
  <main class="postcard">
    <section class="logo-panel">
      <span class="brand-name">LUMERIA</span>
    </section>

    <section class="quote-panel"></section>
    <blockquote class="quote-box">
      <p class="quote-text">“It’s my goal to make every woman<br>feel like her very best self, so she can<br>go out into the world to sparkle and<br>shine. To create a line of jewelry that’s<br>both beautiful and purposeful is truly<br>a dream come true.”</p>
    </blockquote>

    <section class="bio-panel"></section>
    <article class="bio-box">
      <p class="bio-text">• <strong>DR. LENA MARLOW</strong> has had a love affair with jewelry<br>for as long as she can remember. Perhaps it started way<br>back in the day, when she religiously use to look through her<br>grandmother’s jewelry box.</p>
      <p class="bio-text">• Once she got the urge to create, there was no stopping<br>her and the rest, shall we say, is history.</p>
      <p class="bio-text">• She come together with ShopStream to design her very<br>first collection for them called, Jewelry Inspirations by Dr.<br>Lena Collection. This line has timeless symbols, like the hand<br>of Fatima and the evil eye, worn as jewelry for thousands<br>of years to protect, heal and help people to connect more<br>spiritually. The line has a one of a kind look and feel, which is<br>carefully crafted, like fine artisanship, at a modest price point.</p>
      <p class="bio-text">• Her current collection is <strong>LUMERIA</strong> (<em>dream big</em> in<br>spirit). These pieces are based on the bold and dramatic<br>costume pieces of the 60’s and 70’s. Everyone deserves to<br>feel Glamorous and beautiful. This collection is a great way to<br>step into your most stunning self.</p>
    </article>

    <div class="portrait" role="img" aria-label="Portrait photo of the designer, a woman with long blonde hair in a black blazer, against a light grey studio backdrop"></div>
  </main>
</body>
</html>
```